Redesign web application

we are a tele health start up. we need a new design for our platform that allows users, their family and docs to access their detailed stats online
users take readings using our wireless devices that transmit the readings to our server in the background All this happens in real time . and users can instantly login to the portal to view readings , make comments, , view charts,
if readings are not within in prescribed thresholds then alerts are reported on the website, SMS and email
please see the screenshots of existing pages
We need the following pages re designed
login page
patient DB summary , patient DB condition
Doc DB
Nurse DB
After you submit designs and we choose the winning design . please help to make minor modifications after that so that we can use it
Target Market(s)
Paying
Doctors/ Clinics/Clinic chains/ Specialists will be the ones who are paying for the service. the service
Non Paying
patients family members, doctors all will be accessing the system to view readings, alerts , make comments , see charts
Industry/Entity Type
Health
Colors
Designer to choose colors to be used in the design.
Look and feel

```html
<!DOCTYPE html>
<html lang="en">
<head>
<meta charset="utf-8">
<title>VitaLink – Patient Dashboard</title>
<link href="https://fonts.googleapis.com/css2?family=Signika:wght@300;400;600&display=swap" rel="stylesheet">
<style>
:root{
  --page:#d5ebf5;
  --blue:#4fa9d4;
  --blue-dark:#2b8bbd;
  --blue-deep:#1f6f9c;
  --orange:#e8705a;
  --tabs:#e6eaed;
  --content:#f4f5f6;
  --white:#ffffff;
  --text:#4a5560;
  --muted:#8f9aa3;
  --teal:#3aa7a3;
  --link:#5a9dbf;
  --line:#e3e7ea;
  --bp:#d84f51;
  --pulse:#cb7fb1;
}
*{box-sizing:border-box;margin:0;padding:0}
html,body{width:1024px;height:1200px;overflow:hidden}
body{background:var(--page);font-family:"Signika",sans-serif;color:var(--text);position:relative}
.abs{position:absolute}

.brand{left:127px;top:12px;display:flex;align-items:center;gap:6px;font-size:23px;font-weight:600;color:#1c2a36}
.brand-mark{width:14px;height:14px;background:var(--blue-dark)}
.contact{right:120px;top:19px;display:flex;gap:16px;font-size:10px;color:var(--muted)}
.contact span{display:flex;align-items:center;gap:6px}

.panel{left:120px;top:49px;width:784px;height:1078px;background:var(--content);box-shadow:0 1px 4px rgba(0,0,0,.12);overflow:hidden}
.topbar{left:0;top:0;width:784px;height:56px;background:var(--blue)}
.topbar h1{position:absolute;left:21px;top:14px;font-size:16px;font-weight:400;color:#1d5d85}
.topbar .welcome{position:absolute;left:21px;top:33px;font-size:10px;color:var(--white)}
.topbar .welcome u{text-underline-offset:2px}
.howto{position:absolute;left:499px;top:22px;font-size:10px;color:var(--white);display:flex;align-items:center;gap:4px}
.search{position:absolute;left:576px;top:16px;width:159px;height:24px;border-radius:12px;background:var(--white);font-size:9px;color:#a9b3ba;padding:6px 11px}
.search-btn{position:absolute;left:742px;top:14px;width:26px;height:26px;background:var(--blue-dark);border:1px solid #8cc8e6;display:flex;align-items:center;justify-content:center}

.sidebar{left:0;top:56px;width:100px;height:1022px;background:var(--blue);border-right:4px solid #3f96c3}
.nav-item{height:70px;background:var(--blue-dark);color:var(--white);font-size:10px;display:flex;flex-direction:column;align-items:center;justify-content:center;gap:6px;border-bottom:1px solid #2680b0;position:relative}
.nav-item.active{background:var(--orange);border-bottom:0}
.nav-item.active::after{content:"";position:absolute;right:-8px;top:28px;border:7px solid transparent;border-left-color:var(--orange);border-right:0}
.badge{position:absolute;left:7px;top:9px;width:17px;height:17px;border-radius:50%;background:#6cc4c0;border:2px solid #d7eef5;font-size:8px;display:flex;align-items:center;justify-content:center}

.tabs{left:100px;top:56px;width:684px;height:69px;background:var(--tabs)}
.tab{position:absolute;top:10px;height:59px;width:128px;display:flex;flex-direction:column;align-items:center;gap:6px;font-size:9px;color:#9fb0bb;padding-top:4px}
.tab.active{color:var(--orange);border-bottom:3px solid var(--orange)}
.tab.active::after{content:"";position:absolute;bottom:-8px;border:5px solid transparent;border-top-color:var(--orange)}
.tab-sep{position:absolute;top:12px;width:1px;height:40px;background:#d3d9dd}

.patient-name{left:108px;top:155px;font-size:15px;color:#3c4650;display:flex;align-items:center;gap:7px}
.patient-name em{font-style:normal;color:var(--link)}
.add-link{display:flex;align-items:center;gap:10px;color:var(--orange);font-size:15px}
.plus{width:28px;height:28px;background:var(--white);border:1px solid #dde2e6;display:flex;align-items:center;justify-content:center}
.general{right:16px;top:150px}

.card{left:106px;top:184px;width:662px;height:219px;background:var(--white);box-shadow:0 1px 3px rgba(0,0,0,.1)}
.info{position:absolute;left:19px;top:5px;width:320px}
.info-row{display:flex;align-items:center;height:30px;border-bottom:1px solid var(--line);font-size:9.5px}
.info-row:last-child{border-bottom:0}
.info-row .ic{width:24px}
.info-row .lbl{width:103px;color:#4a5560}
.info-row .val{color:var(--link)}
.readings{position:absolute;left:358px;top:5px;width:298px;font-size:9.5px}
.readings .head,.readings .row{height:30px;border-bottom:1px solid var(--line);display:flex;align-items:center}
.readings .head span{display:inline-block}
.readings .row{color:var(--link)}
.dates{position:absolute;left:17px;top:168px;display:flex;align-items:center;font-size:10px}
.date-field{width:129px;height:26px;border:1px solid #d6dce0;display:flex;align-items:center;justify-content:space-between;padding-left:8px;font-size:9.5px;margin:0 6px}
.date-field i{width:24px;height:24px;border-left:1px solid #d6dce0;display:flex;align-items:center;justify-content:center}
.rep{position:absolute;top:168px;height:24px;font-size:9.5px;color:var(--white);display:flex;align-items:center;justify-content:center}
.rep.nu{left:533px;width:58px;background:var(--blue)}
.rep.pat{left:592px;width:59px;background:var(--blue-deep)}

.tile{top:417px;height:118px;color:var(--white);display:flex;align-items:center}
.tile.bp{left:106px;width:333px;background:var(--bp)}
.tile.pulse{left:439px;width:329px;background:var(--pulse)}
.tile .ttl{font-size:14px;font-weight:300;opacity:.85}
.tile .num{font-size:40px;font-weight:300;line-height:1;margin-top:6px}
.tile .num sup{font-size:15px;vertical-align:top;position:relative;top:4px}

.section-title{left:105px;top:562px;font-size:15px;color:#3c4650}
.comment{left:0;width:784px;border-top:1px solid #e6e9eb}
.avatar{position:absolute;left:106px;top:12px;width:51px;height:51px;border-radius:50%;background:radial-gradient(circle at 50% 40%,#e9d3c4,#c9a48c 70%,#eef0f1 72%)}
.author{position:absolute;left:170px;top:23px;font-size:13px;color:var(--teal)}
.stamp{position:absolute;left:170px;top:41px;font-size:9.5px;color:var(--muted)}
.c-action{position:absolute;right:18px;top:22px}
.bubble{position:absolute;left:170px;width:596px;background:var(--white);padding:12px 13px;font-size:9.5px;line-height:1.75;color:var(--link)}
.bubble b{display:block;font-style:italic;font-size:11.5px;color:#4a5560;font-weight:600;margin-bottom:2px}

.pager{left:553px;top:1029px;display:flex;align-items:center;gap:0;font-size:9.5px;color:#5a6670}
.pager span{width:23px;text-align:center}
.pager .cur{width:19px;height:19px;background:var(--blue);color:var(--white);line-height:19px;margin:0 2px}
.pager .next{width:19px;height:19px;border:1px solid #d6dce0;background:var(--white);line-height:17px;margin-left:4px;color:#9aa}
.footer{left:0;width:1024px;top:1144px;text-align:center;font-size:9px;color:#8fa5b2}
</style>
</head>
<body>

<div class="abs brand"><span>VitaLink</span><span class="brand-mark"></span></div>
<div class="abs contact">
  <span><svg width="15" height="10" viewBox="0 0 15 10"><rect x=".5" y=".5" width="14" height="9" fill="none" stroke="#5aa8d3"/><path d="M.5 .5l7 5 7-5" fill="none" stroke="#5aa8d3"/></svg>help@vitalinkcare.net</span>
  <span><svg width="12" height="12" viewBox="0 0 12 12"><path d="M3 1l2 3-1 1c1 2 2 3 3 3l1-1 3 2-1 2C5 11 1 7 1 2z" fill="#5aa8d3"/></svg>Hotline: 5580 2194</span>
</div>

<main class="abs panel">
  <header class="abs topbar">
    <h1>Dashboard</h1>
    <div class="welcome">Welcome, <u>Alex Moran</u></div>
    <div class="howto"><svg width="10" height="10"><circle cx="5" cy="5" r="5" fill="#dceef8"/><text x="5" y="8" font-size="8" text-anchor="middle" fill="#4fa9d4">?</text></svg>Hot to Use</div>
    <div class="search">Search ...</div>
    <div class="search-btn"><svg width="12" height="12" viewBox="0 0 12 12"><circle cx="5" cy="5" r="3.5" fill="none" stroke="#fff" stroke-width="1.6"/><path d="M7.5 7.5L11 11" stroke="#fff" stroke-width="1.8"/></svg></div>
  </header>

  <nav class="abs sidebar">
    <div class="nav-item active"><svg width="30" height="24" viewBox="0 0 30 24"><path d="M15 1L1 13h4v10h7v-7h6v7h7V13h4z" fill="#fff"/></svg>Home</div>
    <div class="nav-item"><span class="badge">4</span><svg width="28" height="22" viewBox="0 0 28 22"><ellipse cx="11" cy="9" rx="10" ry="8" fill="#fff"/><ellipse cx="19" cy="13" rx="8" ry="6.5" fill="#fff" stroke="#2b8bbd" stroke-width="1.5"/><path d="M4 14l-2 6 6-3z" fill="#fff"/></svg>Messages</div>
    <div class="nav-item"><svg width="26" height="20" viewBox="0 0 26 20"><circle cx="6" cy="5" r="3" fill="#fff"/><circle cx="20" cy="5" r="3" fill="#fff"/><circle cx="13" cy="6" r="4" fill="#fff"/><path d="M1 16c0-5 10-5 10 0zM15 16c0-5 10-5 10 0zM6 19c0-7 14-7 14 0z" fill="#fff"/></svg>Patients</div>
    <div class="nav-item"><svg width="24" height="26" viewBox="0 0 24 26"><g stroke="#fff" stroke-width="2.2" fill="#2b8bbd"><path d="M4 1v24M12 1v24M20 1v24"/><circle cx="4" cy="17" r="3"/><circle cx="12" cy="8" r="3"/><circle cx="20" cy="18" r="3"/></g></svg>Settings</div>
    <div class="nav-item"><svg width="26" height="22" viewBox="0 0 26 22"><path d="M3 12h3v8H3zM8 6h3v14H8zM13 2h3v18h-3zM18 9h3v11h-3z M1 20h24v2H1z" fill="#fff"/></svg>Statistics</div>
    <div class="nav-item"><svg width="24" height="24" viewBox="0 0 24 24"><path d="M7 5a9 9 0 1 0 10 0" fill="none" stroke="#fff" stroke-width="2.6"/><path d="M12 1v10" stroke="#fff" stroke-width="2.6"/></svg>Logout</div>
  </nav>

  <div class="abs tabs">
    <div class="tab" style="left:0"><svg width="24" height="20" viewBox="0 0 24 20"><path d="M2 10h3v9H2zM7 5h3v14H7zM12 1h3v18h-3zM17 8h3v11h-3zM0 19h24v1H0z" fill="#a9bfcc"/></svg>Summary</div>
    <div class="tab-sep" style="left:131px"></div>
    <div class="tab active" style="left:132px"><svg width="18" height="24" viewBox="0 0 18 24"><path d="M9 1C6 8 1 12 1 16a8 8 0 0 0 16 0c0-4-5-8-8-15z" fill="#e8705a"/></svg>Blood Pressure</div>
    <div class="tab-sep" style="left:260px"></div>
    <div class="tab" style="left:261px"><svg width="16" height="28" viewBox="0 0 16 28"><rect x="1" y="1" width="14" height="19" rx="5" fill="none" stroke="#a9bfcc" stroke-width="2"/><rect x="4" y="5" width="8" height="7" fill="#a9bfcc"/><path d="M8 20v7" stroke="#a9bfcc" stroke-width="2"/></svg>Blood Glucose</div>
    <div class="tab-sep" style="left:391px"></div>
    <div class="tab" style="left:392px"><svg width="22" height="22" viewBox="0 0 22 22"><rect x="1" y="1" width="20" height="20" rx="2" fill="#a9bfcc"/><rect x="4" y="4" width="14" height="6" fill="#e6eaed"/><path d="M11 9l2-3" stroke="#a9bfcc" stroke-width="1.5"/></svg>Body Weight</div>
    <div class="tab-sep" style="left:520px"></div>
  </div>

  <div class="abs patient-name"><svg width="12" height="12" viewBox="0 0 12 12"><circle cx="6" cy="3" r="2.6" fill="#5aa8d3"/><path d="M0 12c1-6 11-6 12 0z" fill="#5aa8d3"/></svg>Name of Patient: <em>Tan Wei Ling</em></div>
  <div class="abs add-link general">Add General Comment<span class="plus"><svg width="12" height="12"><path d="M6 0v12M0 6h12" stroke="#e8705a" stroke-width="2.4"/></svg></span></div>

  <section class="abs card">
    <div class="info">
      <div class="info-row"><span class="ic"><svg width="9" height="12"><rect x=".5" y=".5" width="8" height="11" rx="1" fill="none" stroke="#5aa8d3"/><rect x="2" y="2" width="5" height="5" fill="#5aa8d3"/></svg></span><span class="lbl">Contact:</span><span class="val">(02) 514-3370(HP) ; 02) 592-8841(HO)</span></div>
      <div class="info-row"><span class="ic"><svg width="12" height="12"><path d="M1 0v12" stroke="#5aa8d3" stroke-width="1.5"/><path d="M2 1h9l-2 3 2 3H2z" fill="#5aa8d3"/></svg></span><span class="lbl">NRIC#:</span><span class="val">S1234H</span></div>
      <div class="info-row"><span class="ic"><svg width="11" height="12"><rect width="11" height="12" fill="#8fc4e0"/><path d="M2 3h7M2 6h7M2 9h7" stroke="#fff"/></svg></span><span class="lbl">Patient of Dept:</span><span class="val">Cardio-AMI, UAT1</span></div>
      <div class="info-row"><span class="ic"><svg width="13" height="12"><circle cx="6.5" cy="3" r="3" fill="#5aa8d3"/><path d="M0 12c1-6 12-6 13 0z" fill="#5aa8d3"/></svg></span><span class="lbl">Patient Type:</span><span class="val">Surveillance</span></div>
      <div class="info-row"><span class="ic"><svg width="13" height="13"><circle cx="6.5" cy="3.5" r="3" fill="#5aa8d3"/><path d="M0 13c1-6 12-6 13 0z" fill="#5aa8d3"/><path d="M6.5 8v4M4.5 10h4" stroke="#fff" stroke-width="1.2"/></svg></span><span class="lbl">Primary Physician:</span><span class="val">Chen Hao Ran</span></div>
    </div>
    <div class="readings">
      <div class="head"><span style="width:59px">Date</span><span style="width:58px">Time</span><span style="width:65px">Systolic</span><span style="width:67px">Diastolic</span><span>Pulse</span></div>
      <div class="row">No Results Found.</div>
      <div class="row"></div>
      <div class="row"></div>
      <div class="row"></div>
    </div>
    <div class="dates">From
      <span class="date-field">2014-06-15<i><svg width="14" height="13"><rect y="2" width="14" height="11" fill="#2b8bbd"/><path d="M2 6h10M2 9h10M5 4v8M9 4v8" stroke="#fff" stroke-width=".8"/><path d="M4 0v3M10 0v3" stroke="#2b8bbd" stroke-width="1.5"/></svg></i></span>
      <span style="margin-left:8px">To</span>
      <span class="date-field" style="width:130px">2014-06-15<i><svg width="14" height="13"><rect y="2" width="14" height="11" fill="#2b8bbd"/><path d="M2 6h10M2 9h10M5 4v8M9 4v8" stroke="#fff" stroke-width=".8"/><path d="M4 0v3M10 0v3" stroke="#2b8bbd" stroke-width="1.5"/></svg></i></span>
    </div>
    <div class="rep nu">NU Rep</div>
    <div class="rep pat">Pat Rep</div>
  </section>

  <div class="abs tile bp">
    <svg style="margin:0 19px 0 23px" width="42" height="64" viewBox="0 0 42 64"><path d="M21 0C14 20 1 30 1 43a20 20 0 0 0 40 0C41 30 28 20 21 0z" fill="#fff"/></svg>
    <div><div class="ttl">Blood Pressure</div><div class="num">128/78</div></div>
  </div>
  <div class="abs tile pulse">
    <svg style="margin:0 14px 0 27px" width="80" height="66" viewBox="0 0 80 66"><path d="M0 35h32l6-10 7-25 8 64 7-29h20" fill="none" stroke="#fff" stroke-width="5" stroke-linejoin="round"/></svg>
    <div><div class="ttl">Pulse</div><div class="num">40<sup>BPM</sup></div></div>
  </div>

  <h2 class="abs section-title" style="font-weight:400">Recent Comments</h2>

  <article class="abs comment" style="top:596px;height:153px">
    <div class="avatar" role="img" aria-label="Portrait photo of the nurse who wrote the comment"></div>
    <div class="author">UAT Nurse</div>
    <div class="stamp">Jun-05-2014 | &nbsp;12:35pm</div>
    <div class="c-action add-link" style="font-size:15px">Add Standing Order<span class="plus"><svg width="12" height="12"><path d="M6 0v12M0 6h12" stroke="#e8705a" stroke-width="2.4"/></svg></span></div>
    <div class="bubble" style="top:59px;height:76px"><b>Standing Order BP:</b>Dolore magna aliqua. Duis aute irure dolor in reprehenderit in voluptate velit esse cillum dolore eu fugiat nulla pariatur. Ut enim ad minim veniam...</div>
  </article>

  <article class="abs comment" style="top:749px;height:136px">
    <div class="avatar" role="img" aria-label="Portrait photo of the nurse who wrote the comment"></div>
    <div class="author">UAT Nurse</div>
    <div class="stamp">Jun-05-2014 | &nbsp;12:35pm</div>
    <div class="c-action add-link">Add Patient Notes<span class="plus"><svg width="12" height="12"><path d="M6 0v12M0 6h12" stroke="#e8705a" stroke-width="2.4"/></svg></span></div>
    <div class="bubble" style="top:59px;height:57px"><b>Confidential Patient Notes:</b>Lorem ipsum dolor sit amet, consectetur adipisicing elit, sed do eiusmod tempor incididunt ut labore et dolore magna</div>
  </article>

  <article class="abs comment" style="top:885px;height:140px">
    <div class="avatar" role="img" aria-label="Portrait photo of the nurse who wrote the comment"></div>
    <div class="author">UAT Nurse</div>
    <div class="stamp">Jun-05-2014 | &nbsp;12:35pm</div>
    <div class="c-action add-link">Add Patient Notes<span class="plus"><svg width="12" height="12"><path d="M6 0v12M0 6h12" stroke="#e8705a" stroke-width="2.4"/></svg></span></div>
    <div class="bubble" style="top:59px;height:57px"><b>Standing Order BP:</b>Dolore magna aliqua. Duis aute irure dolor in reprehenderit in voluptate velit esse cillum dolore eu fugiat nulla pariatur.</div>
  </article>

  <nav class="abs pager"><span>1</span><span class="cur">2</span><span>3</span><span>4</span><span>5</span><span>6</span><span>7</span><span>...</span><span>15</span><span class="next">›</span></nav>
</main>

<footer class="abs footer">Copyright 2014 © VitaLink. All Rights Reserved.</footer>
</body>
</html>
```